Need a sleek, professional business card design for a Web Development business

I need a unique business card designed for a web development company. It is also the parent company for any ventures I do, such as my ClipHarbor channel, startup ideas I have, etc. I am the single member of "Copper Lantern Sites LLC." I will attach my basic logo here, so you will see the current color scheme and have the asset available. Thank you!

Target Market(s)

Startups, SMB's, Professionals

Industry/Entity Type

Business

Font styles to use
Other font styles liked:
• Lovello for headings is what I use, but not necessary.

Colors

Designer to choose colors to be used in the design.

Requirements
Nice to have
• Sleek is the word. Professional, modern, dark.
Should not have
• Any work from someone else's design. Lacking originality.

```html
<!DOCTYPE html>
<html lang="en">
<head>
<meta charset="utf-8">
<title>Copper Lantern Sites LLC – Business Card</title>
<link rel="stylesheet" href="https://fonts.googleapis.com/css2?family=Bebas+Neue&family=Work+Sans:wght@300;400&display=swap">
<style>
  :root {
    --page-bg: #ece8e3;
    --card-frost: #dcd7d0;
    --card-edge: #c9c3bb;
    --panel-dark-start: #262626;
    --panel-dark-end: #3a3937;
    --copper: #c98a55;
    --copper-deep: #d9673f;
    --text-light: #d6d3cf;
  }
  * { margin: 0; padding: 0; box-sizing: border-box; }
  html, body {
    width: 1200px;
    height: 1047px;
    overflow: hidden;
    background: var(--page-bg);
  }
  .card {
    position: absolute;
    left: 100px;
    top: 252px;
    width: 1000px;
    height: 542px;
    border-radius: 18px;
    overflow: hidden;
    background: var(--card-frost);
    box-shadow: 0 0 0 1px var(--card-edge), 0 18px 40px rgba(0,0,0,0.12);
  }
  .card-panel {
    position: absolute;
    inset: 0;
    width: 1000px;
    height: 542px;
  }
  .company-heading {
    position: absolute;
    left: 54px;
    top: 60px;
    font-family: "Bebas Neue", sans-serif;
    font-size: 56px;
    line-height: 1;
    letter-spacing: 1px;
    color: var(--copper);
  }
  .person-name {
    position: absolute;
    left: 54px;
    top: 258px;
    font-family: "Work Sans", sans-serif;
    font-weight: 400;
    font-size: 38px;
    line-height: 1;
    letter-spacing: 3px;
    color: var(--copper);
  }
  .person-role,
  .address {
    position: absolute;
    left: 54px;
    font-family: "Work Sans", sans-serif;
    font-weight: 300;
    font-size: 21px;
    color: var(--text-light);
  }
  .person-role { top: 302px; }
  .address { top: 346px; line-height: 29px; }
  .contact-list {
    position: absolute;
    left: 54px;
    top: 415px;
    list-style: none;
    font-family: "Work Sans", sans-serif;
    font-weight: 300;
    font-size: 21px;
    line-height: 29px;
    color: var(--text-light);
  }
  .contact-item { display: flex; align-items: center; gap: 14px; }
  .contact-icon { width: 14px; height: 14px; flex: none; }
  .contact-highlight { color: var(--copper); }
  .brand-mark {
    position: absolute;
    left: 690px;
    top: 190px;
    width: 270px;
    display: flex;
    flex-direction: column;
    align-items: center;
    gap: 18px;
  }
  .brand-dot {
    width: 74px;
    height: 74px;
    border-radius: 50%;
    background: var(--copper-deep);
  }
  .brand-name {
    font-family: "Bebas Neue", sans-serif;
    font-size: 40px;
    line-height: 1.05;
    text-align: center;
    color: var(--copper-deep);
  }
</style>
</head>
<body>
  <div class="card">
    <svg class="card-panel" viewBox="0 0 1000 542" aria-hidden="true">
      <defs>
        <linearGradient id="panelShade" x1="0" y1="0" x2="1" y2="0">
          <stop offset="0" stop-color="var(--panel-dark-start)"/>
          <stop offset="1" stop-color="var(--panel-dark-end)"/>
        </linearGradient>
      </defs>
      <path d="M0 0 H665 C640 40 620 110 600 170 C570 240 540 300 560 380 C575 450 600 500 625 542 H0 Z" fill="url(#panelShade)"/>
    </svg>

    <div class="company-heading">Copper Lantern Sites LLC.</div>

    <div class="person-name">MARLON KEEL</div>
    <div class="person-role">Managing Partner</div>
    <div class="address">Kastanienweg 18, 74821<br>Mosbach, Germany</div>

    <ul class="contact-list">
      <li class="contact-item">
        <svg class="contact-icon" viewBox="0 0 14 14" aria-hidden="true"><path d="M3 1 L5 4 L4 5.5 C5 7.5 6.5 9 8.5 10 L10 9 L13 11 L12 13 C6 13 1 8 1 2 Z" fill="var(--copper)"/></svg>
        <span>+49 170 482 306 17</span>
      </li>
      <li class="contact-item">
        <svg class="contact-icon" viewBox="0 0 14 14" aria-hidden="true"><rect x="1" y="3" width="12" height="8" fill="none" stroke="var(--copper)" stroke-width="1.4"/><path d="M1 3 L7 8 L13 3" fill="none" stroke="var(--copper)" stroke-width="1.4"/></svg>
        <span>hello@copperlantern.com</span>
      </li>
      <li class="contact-item">
        <svg class="contact-icon" viewBox="0 0 14 14" aria-hidden="true"><circle cx="7" cy="7" r="5.5" fill="none" stroke="var(--copper)" stroke-width="1.3"/><ellipse cx="7" cy="7" rx="2.3" ry="5.5" fill="none" stroke="var(--copper)" stroke-width="1"/><path d="M1.5 7 H12.5" stroke="var(--copper)" stroke-width="1"/></svg>
        <span>www.<span class="contact-highlight">copperlantern</span>.com</span>
      </li>
    </ul>

    <div class="brand-mark">
      <div class="brand-dot"></div>
      <div class="brand-name">Copper Lantern<br>Sites LLC</div>
    </div>
  </div>
</body>
</html>
```